Launching new podcast and need artwork

we are two guys in our early 40's from east Texas who are starting a podcast around personal finance.

The title of the podcast will be "Ledger Gripes" and the subtitle will be "Financial hacks with some southern charm"

We own the company boundlessdaysplanning.example and will be using the podcast as a lead generation for our primary business of financial coaching.

Target Market(s)

Male 35-45 years old

Industry/Entity Type

Personal finance

Requirements
Nice to have
• Rugged or rustic feel would fit our personas

```html
<!DOCTYPE html>
<html lang="en">
<head>
<meta charset="utf-8">
<title>Ledger Gripes Podcast – Cover Art</title>
<link rel="stylesheet" href="https://fonts.googleapis.com/css2?family=Bebas+Neue&display=swap">
<style>
  :root {
    --backdrop: #cbcbcb;
    --charcoal: #241f1d;
    --ember: #ff3d00;
    --ember-deep: #c93208;
    --chalk: #ffffff;
  }
  html, body {
    margin: 0;
    padding: 0;
    width: 1183px;
    height: 1200px;
    overflow: hidden;
    background: var(--backdrop);
  }
  .cover {
    position: absolute;
    left: 0;
    top: 8px;
    width: 1183px;
    height: 1183px;
    display: block;
  }
  .cover text {
    font-family: "Bebas Neue", "Oswald", sans-serif;
  }
  .title-outline { fill: none; stroke: var(--chalk); stroke-width: 2.5; }
  .title-hacks { fill: var(--ember); }
  .tag-text { fill: var(--charcoal); }
  .title-charm { fill: var(--chalk); }
  .show-name { fill: var(--chalk); }
  .show-kind { fill: var(--chalk); }
</style>
</head>
<body>
<svg class="cover" viewBox="0 0 1410 1410" xmlns="http://www.w3.org/2000/svg">
  <defs>
    <linearGradient id="rugged-fade" x1="0" y1="0" x2="0" y2="1">
      <stop offset="0" stop-color="var(--charcoal)"/>
      <stop offset="0.2" stop-color="#6e2710"/>
      <stop offset="0.55" stop-color="var(--ember-deep)"/>
      <stop offset="1" stop-color="var(--ember)"/>
    </linearGradient>
  </defs>

  <!-- panel -->
  <rect class="panel" width="1410" height="1410" fill="var(--charcoal)"/>

  <!-- growth line -->
  <polyline class="growth-line" points="0,331 158,253 469,238 655,13 1004,110 1410,0"
            fill="none" stroke="var(--ember)" stroke-width="6" stroke-linejoin="miter"/>

  <!-- accent bar -->
  <rect class="accent-bar" x="145" y="316" width="51" height="288" fill="var(--ember)"/>

  <!-- headline -->
  <text class="title-outline" x="250" y="436" font-size="176" textLength="571" lengthAdjust="spacingAndGlyphs">FINANCIAL</text>
  <text class="title-hacks" x="248" y="655" font-size="284" textLength="577" lengthAdjust="spacingAndGlyphs">HACKS</text>

  <!-- hatched block area -->
  <rect class="hatch-block" x="867" y="296" width="397" height="205" fill="var(--ember)"
        role="img" aria-label="Diagonal orange stripe pattern block"/>

  <!-- tag -->
  <rect class="tag-box" x="867" y="516" width="397" height="129" fill="var(--chalk)"/>
  <text class="tag-text" x="888" y="615" font-size="103" textLength="355" lengthAdjust="spacingAndGlyphs">WITH SOME</text>

  <text class="title-charm" x="250" y="813" font-size="176" textLength="1017" lengthAdjust="spacingAndGlyphs">SOUTHERN CHARM</text>

  <!-- rugged lower band -->
  <rect class="rugged-band" x="0" y="948" width="1410" height="162" fill="url(#rugged-fade)"
        role="img" aria-label="Distressed grunge texture in orange and charcoal"/>
  <rect class="base-band" x="0" y="1108" width="1410" height="302" fill="var(--ember)"/>

  <!-- show name -->
  <rect class="name-frame" x="337.5" y="1102.5" width="735" height="150" fill="none" stroke="var(--chalk)" stroke-width="5"/>
  <text class="show-name" x="378" y="1226" font-size="136" textLength="655" lengthAdjust="spacingAndGlyphs">LEDGER GRIPES</text>

  <text class="show-kind" x="465" y="1329" font-size="76" textLength="480" lengthAdjust="spacing">PODCAST</text>
</svg>
</body>
</html>
```